Harrow's Electrical & Solar - Business Cards

I want my business card to stand out from the rest. I will provide my business name logo and my icon logo to be implemented onto the card.

On the front of the card, can i have the following. Just make it neat & professional please.

Liam Corbett
harrowselectrical@quillmail.test
0438 917 605
ABN: 41 602 719 384
License No. 582164K
FREE QUOTES
24/7 Emergency

On the back of the card, can I have "Our Services" and maybe add the S logo on the back in the background or something. Under "Our Services" I want the following:

LED Lighting Upgrades
Switches & Outlets
Smoke Alarms
Switchboard Upgrades
Fault Finding
Rewiring
New Builds
Test & Tagging
All Electrical Maintenance & Repairs

Can you guys add the instagram logo and next to it, put harrows_electrical

Can you guys also add the facebook logo and next to it put Harrow's Electrical & Solar. Make sure the instagram & facebook icon is in either white, green or black.

Also I have put down double sided, not sure why when i save it, it keeps going to single sided. I need my business card double sided.

Target Market(s)

New Customers

Contact Information for Business Card

Liam Corbett harrowselectrical@quillmail.test 0438 917 605 ABN: 41 602 719 384 License No. 582164K FREE QUOTES 24/7 Emergency

Requirements
Must have
• must be tidy, professional and appealing

```html
<!DOCTYPE html>
<html lang="en">
<head>
<meta charset="utf-8">
<title>Harrow's Electrical &amp; Solar – Business Cards</title>
<link href="https://fonts.googleapis.com/css2?family=Montserrat:wght@500;700&family=Oswald:wght@500;600&display=swap" rel="stylesheet">
<style>
  :root {
    --green: #22b53c;
    --green-bright: #35d04f;
    --ink: #161616;
    --paper: #ffffff;
    --paper-shade: #f1f1f1;
    --steel: #a9adb3;
    --steel-light: #d9dce0;
    --card-black: #0c0c0c;
    --on-dark: #f2f2f2;
    --backdrop: #3a3a3a;
  }
  * { box-sizing: border-box; margin: 0; padding: 0; }
  html, body { width: 1200px; height: 1200px; overflow: hidden; }
  body {
    background: var(--backdrop);
    font-family: "Montserrat", Arial, sans-serif;
    color: var(--ink);
    position: relative;
  }
  .card {
    position: absolute;
    left: 150px;
    width: 900px;
    height: 514px;
    border-radius: 34px;
    overflow: hidden;
  }

  /* ---------- front ---------- */
  .card-front {
    top: 52px;
    background: linear-gradient(180deg, var(--paper) 0%, var(--paper) 60%, var(--paper-shade) 100%);
  }
  .brand-name {
    position: absolute;
    left: 58px;
    top: 96px;
    display: flex;
    align-items: center;
    gap: 14px;
    font-weight: 700;
    font-size: 30px;
    line-height: 1.05;
    color: var(--green);
    text-transform: uppercase;
    letter-spacing: 0.5px;
  }
  .brand-dot {
    width: 40px; height: 40px; border-radius: 50%;
    background: var(--green);
    flex: none;
  }
  .contact {
    position: absolute;
    left: 58px;
    top: 222px;
  }
  .person-name {
    font-weight: 700;
    font-size: 38px;
    color: var(--green);
    text-transform: uppercase;
    margin-bottom: 12px;
  }
  .contact-line {
    display: flex;
    align-items: center;
    gap: 12px;
    font-weight: 500;
    font-size: 24px;
    margin-bottom: 8px;
  }
  .contact-line svg { width: 24px; height: 24px; flex: none; }
  .registration {
    margin-top: 18px;
    font-weight: 500;
    font-size: 22px;
    line-height: 1.3;
  }
  .availability {
    position: absolute;
    right: 64px;
    top: 96px;
    display: flex;
    align-items: center;
    gap: 14px;
  }
  .availability svg { width: 56px; height: 56px; }
  .free-quotes {
    font-weight: 700;
    font-size: 24px;
    color: var(--green);
    text-transform: uppercase;
  }
  .emergency { font-weight: 500; font-size: 20px; }
  .emergency strong { font-weight: 700; font-size: 32px; margin-right: 6px; }
  .band-green {
    position: absolute;
    left: 0; bottom: 0;
    width: 585px; height: 34px;
    background: linear-gradient(90deg, var(--green) 0%, var(--green-bright) 100%);
    clip-path: polygon(0 100%, 0 60%, 100% 0, 100% 100%);
  }
  .band-steel {
    position: absolute;
    right: 0; bottom: 0;
    width: 300px; height: 46px;
    background: linear-gradient(90deg, var(--steel) 0%, var(--steel-light) 60%, var(--steel) 100%);
  }

  /* ---------- back ---------- */
  .card-back {
    top: 628px;
    background: radial-gradient(circle at 30% 45%, #1c1c1c 0%, var(--card-black) 60%);
    color: var(--on-dark);
  }
  .back-ring {
    position: absolute;
    left: 110px;
    top: 70px;
    width: 230px; height: 230px; border-radius: 50%;
    border: 14px solid var(--green);
  }
  .back-brand {
    position: absolute;
    left: 50px;
    top: 330px;
    width: 350px;
    text-align: center;
    font-weight: 700;
    font-size: 30px;
    line-height: 1.1;
    color: var(--green);
    text-transform: uppercase;
  }
  .services {
    position: absolute;
    left: 470px;
    top: 44px;
    font-family: "Oswald", "Arial Narrow", sans-serif;
    text-transform: uppercase;
  }
  .services-title {
    font-weight: 600;
    font-size: 30px;
    color: var(--green);
    margin-bottom: 6px;
  }
  .services-list { list-style: none; }
  .services-list li {
    font-weight: 500;
    font-size: 21px;
    line-height: 1.22;
    padding-left: 20px;
    position: relative;
  }
  .services-list li::before {
    content: "";
    position: absolute;
    left: 2px; top: 11px;
    width: 8px; height: 8px; border-radius: 50%;
    background: var(--green);
  }
  .services-list li.continued::before { display: none; }
  .social {
    position: absolute;
    left: 50px;
    right: 50px;
    bottom: 30px;
    display: flex;
    justify-content: center;
    gap: 48px;
    font-weight: 500;
    font-size: 18px;
  }
  .social-item { display: flex; align-items: center; gap: 10px; }
  .social-mark {
    width: 22px; height: 22px; border-radius: 50%;
    background: var(--green);
    flex: none;
  }
</style>
</head>
<body>

<section class="card card-front" aria-label="Business card front">
  <div class="brand-name">
    <span class="brand-dot"></span>
    <span>Harrow's<br>Electrical &amp; Solar</span>
  </div>

  <div class="availability">
    <svg viewBox="0 0 48 48" aria-hidden="true"><circle cx="24" cy="24" r="20" fill="none" stroke="#22b53c" stroke-width="4"/><path d="M24 12v13h9" fill="none" stroke="#22b53c" stroke-width="4" stroke-linecap="round"/></svg>
    <div>
      <p class="free-quotes">Free Quotes</p>
      <p class="emergency"><strong>24/7</strong>Emergency</p>
    </div>
  </div>

  <div class="contact">
    <p class="person-name">Liam Corbett</p>
    <p class="contact-line">
      <svg viewBox="0 0 24 24" aria-hidden="true"><path fill="#22b53c" d="M6.6 10.8a15 15 0 0 0 6.6 6.6l2.2-2.2c.3-.3.7-.4 1-.2 1.1.4 2.3.6 3.6.6.6 0 1 .4 1 1V20c0 .6-.4 1-1 1A17 17 0 0 1 3 4c0-.6.4-1 1-1h3.5c.6 0 1 .4 1 1 0 1.3.2 2.5.6 3.6.1.3 0 .7-.2 1z"/></svg>
      0438 917 605
    </p>
    <p class="contact-line">
      <svg viewBox="0 0 24 24" aria-hidden="true"><rect x="2" y="5" width="20" height="14" fill="#22b53c"/><path d="M2 5l10 8 10-8" fill="none" stroke="#fff" stroke-width="1.6"/></svg>
      harrowselectrical@quillmail.test
    </p>
    <p class="registration">ABN: 41 602 719 384<br>License Nº 582164K</p>
  </div>

  <div class="band-green"></div>
  <div class="band-steel"></div>
</section>

<section class="card card-back" aria-label="Business card back">
  <div class="back-ring"></div>
  <p class="back-brand">Harrow's<br>Electrical &amp; Solar</p>

  <div class="services">
    <h2 class="services-title">Our Services</h2>
    <ul class="services-list">
      <li>LED Lighting Upgrades</li>
      <li>Switches &amp; Outlets</li>
      <li>Smoke Alarms</li>
      <li>Switchboard Upgrades</li>
      <li>Fault Finding</li>
      <li>Rewiring</li>
      <li>New Builds</li>
      <li>Test &amp; Tagging</li>
      <li>All Electrical</li>
      <li class="continued">Maintenance &amp; Repairs</li>
    </ul>
  </div>

  <div class="social">
    <p class="social-item"><span class="social-mark"></span>harrows_electrical</p>
    <p class="social-item"><span class="social-mark"></span>Harrow's Electrical &amp; Solar</p>
  </div>
</section>

</body>
</html>
```